out of the box Business Card Design for a Manufacturer / Distributor

We are a manufarturer and distributor of products.
the company name is VOLMINTA (Pic attached)

the picture is NOT a must have on the business Card.

the Business Card should look really professional and/or special, so out of the box thinking is welcome.

there should be 2 Adresses on the Business Card for Main and Branch Office.
Email Adress, homepage, Name is required
NO Phone Number

Our working field:
Private Labeling
high Quality Production
direct distribution
warehousing
trademark registration
legal support

Main Office:
Ulmenweg 7
04683 Kesselbrunn
Germany

Branch Office:
Kotli Lane
Mehranwal
Pakistan

Names:
Bernd Kellhofer (Owner)
Farhan Qureshi (Owner)

Email:
bernd@volminta-example.com
farhan@volminta-example.com

homepage:
volminta-example.com

Industry/Entity Type

Manufacturer Distributer

Contact Information for Business Card

Volminta

Requirements
Must have
• Names, both office Adresses, email, homepage
Should not have
• Phone Number

```html
<!DOCTYPE html>
<html lang="en">
<head>
<meta charset="utf-8">
<title>Volminta Business Card</title>
<link rel="stylesheet" href="https://fonts.googleapis.com/css2?family=Poppins:wght@400;500;600&display=swap">
<style>
  :root {
    --paper: #ffffff;
    --backdrop: #f4f4f4;
    --ink: #111111;
    --ink-soft: #3b3b3b;
    --accent: #f26b4c;
    --accent-pink: #f47c98;
    --accent-purple: #9a5bd0;
    --watermark: #efefef;
    --divider: #dddddd;
  }
  html, body {
    margin: 0;
    padding: 0;
    width: 1200px;
    height: 2527px;
    overflow: hidden;
    background: var(--backdrop);
    font-family: "Poppins", sans-serif;
  }
  .sheet {
    position: relative;
    width: 1200px;
    height: 2527px;
  }
  .card {
    position: absolute;
    left: 100px;
    width: 1000px;
    height: 571px;
    background: var(--paper);
    box-shadow: 0 6px 18px rgba(0,0,0,0.18);
    overflow: hidden;
  }
  .card svg { display: block; width: 100%; height: 100%; }
  .card--front { top: 652px; }
  .card--back { top: 1303px; }
  .wordmark { font-family: "Poppins", sans-serif; font-weight: 400; fill: var(--ink); }
  .section-title { font-weight: 500; fill: var(--accent); }
  .service { font-weight: 400; fill: var(--ink); font-size: 17px; }
  .person-name { font-weight: 500; fill: var(--ink-soft); font-size: 29px; }
  .person-role { font-weight: 500; fill: var(--accent); font-size: 14px; letter-spacing: 7px; }
  .contact { font-weight: 400; fill: var(--ink-soft); font-size: 17px; }
  .office-title { font-weight: 500; fill: var(--accent); font-size: 15px; }
  .address { font-weight: 400; fill: var(--ink-soft); font-size: 13px; }
  .icon { fill: var(--accent); }
  .icon-line { stroke: var(--accent); fill: none; }
</style>
</head>
<body>
<main class="sheet">

  <section class="card card--front" aria-label="Business card front">
    <svg viewBox="0 0 840 480" xmlns="http://www.w3.org/2000/svg">
      <defs>
        <linearGradient id="halo-gradient" x1="0" y1="0" x2="0" y2="1">
          <stop offset="0" stop-color="var(--accent-pink)"/>
          <stop offset="0.45" stop-color="#fb9f82"/>
          <stop offset="1" stop-color="var(--accent-purple)"/>
        </linearGradient>
        <linearGradient id="wave-gradient" x1="0" y1="0" x2="1" y2="0">
          <stop offset="0" stop-color="#f0304f"/>
          <stop offset="0.4" stop-color="var(--accent)"/>
          <stop offset="0.75" stop-color="#d0507a"/>
          <stop offset="1" stop-color="#7a2fc4"/>
        </linearGradient>
      </defs>
      <rect width="840" height="480" fill="var(--paper)"/>
      <circle class="halo" cx="860" cy="195" r="230" fill="url(#halo-gradient)" opacity="0.9"/>
      <path class="wave" d="M0 420 C30 400 70 385 100 385 S220 460 300 460 S440 385 495 385 S640 500 720 500 S810 480 840 450" fill="none" stroke="url(#wave-gradient)" stroke-width="3"/>
      <circle class="brand-dot" cx="84" cy="226" r="26" fill="var(--ink)"/>
      <text class="wordmark" x="128" y="246" font-size="54">VOLMINTA</text>
    </svg>
  </section>

  <section class="card card--back" aria-label="Business card back">
    <svg viewBox="0 0 840 480" xmlns="http://www.w3.org/2000/svg">
      <rect width="840" height="480" fill="var(--paper)"/>
      <circle class="watermark" cx="850" cy="215" r="175" fill="var(--watermark)"/>
      <line class="divider" x1="392" y1="30" x2="392" y2="440" stroke="var(--divider)" stroke-width="2"/>

      <circle class="brand-dot" cx="78" cy="103" r="18" fill="var(--ink)"/>
      <text class="wordmark" x="106" y="117" font-size="38">VOLMINTA</text>

      <text class="section-title" x="60" y="206" font-size="23">OUR WORKING FIELD</text>
      <g class="services">
        <g transform="translate(68,238)"><circle class="icon" r="6"/><path d="M-3 0 l2 2.5 l4 -4.5" stroke="#fff" stroke-width="1.6" fill="none"/></g>
        <text class="service" x="102" y="244">Private Labeling</text>
        <g transform="translate(68,272)"><circle class="icon" r="6"/><path d="M-3 0 l2 2.5 l4 -4.5" stroke="#fff" stroke-width="1.6" fill="none"/></g>
        <text class="service" x="102" y="278">High Quality Production</text>
        <g transform="translate(68,304)"><circle class="icon" r="6"/><path d="M-3 0 l2 2.5 l4 -4.5" stroke="#fff" stroke-width="1.6" fill="none"/></g>
        <text class="service" x="102" y="310">Direct distribution</text>
        <g transform="translate(68,338)"><circle class="icon" r="6"/><path d="M-3 0 l2 2.5 l4 -4.5" stroke="#fff" stroke-width="1.6" fill="none"/></g>
        <text class="service" x="102" y="344">Warehousing</text>
        <g transform="translate(68,372)"><circle class="icon" r="6"/><path d="M-3 0 l2 2.5 l4 -4.5" stroke="#fff" stroke-width="1.6" fill="none"/></g>
        <text class="service" x="102" y="378">Trademark registration</text>
        <g transform="translate(68,406)"><circle class="icon" r="6"/><path d="M-3 0 l2 2.5 l4 -4.5" stroke="#fff" stroke-width="1.6" fill="none"/></g>
        <text class="service" x="102" y="412">Legal support</text>
      </g>

      <g class="person">
        <text class="person-name" x="460" y="96">Bernd Kellhofer</text>
        <text class="person-role" x="463" y="122">OWNER</text>
        <g transform="translate(460,137)"><rect class="icon" width="20" height="15" rx="2"/><path d="M1 2 l9 6 l9 -6" stroke="#fff" stroke-width="1.5" fill="none"/></g>
        <text class="contact" x="489" y="150">bernd@volminta-example.com</text>
      </g>
      <g class="person">
        <text class="person-name" x="460" y="207">Farhan Qureshi</text>
        <text class="person-role" x="463" y="231">OWNER</text>
        <g transform="translate(460,244)"><rect class="icon" width="20" height="15" rx="2"/><path d="M1 2 l9 6 l9 -6" stroke="#fff" stroke-width="1.5" fill="none"/></g>
        <text class="contact" x="489" y="257">farhan@volminta-example.com</text>
      </g>

      <g class="office">
        <text class="office-title" x="454" y="306">MAIN OFFICE</text>
        <g transform="translate(464,326)"><path class="icon-line" stroke-width="1.8" d="M0 10 C-8 2 -8 -9 0 -9 C8 -9 8 2 0 10 Z"/><circle class="icon" cy="-2" r="2.5"/></g>
        <text class="address" x="486" y="326">Ulmenweg 7</text>
        <text class="address" x="486" y="342">04683 Kesselbrunn</text>
        <text class="address" x="486" y="358">Germany</text>
      </g>
      <g class="office">
        <text class="office-title" x="640" y="306">BRANCH OFFICE</text>
        <g transform="translate(651,326)"><path class="icon-line" stroke-width="1.8" d="M0 10 C-8 2 -8 -9 0 -9 C8 -9 8 2 0 10 Z"/><circle class="icon" cy="-2" r="2.5"/></g>
        <text class="address" x="670" y="326">Kotli Lane</text>
        <text class="address" x="670" y="342">Mehranwal</text>
        <text class="address" x="670" y="358">Pakistan</text>
      </g>

      <g class="website">
        <g transform="translate(466,403)" class="icon-line" stroke-width="1.6">
          <circle r="9"/><ellipse rx="4" ry="9"/><line x1="-9" x2="9"/>
        </g>
        <text class="contact" x="486" y="409">volminta-example.com</text>
      </g>
    </svg>
  </section>

</main>
</body>
</html>
```